Flyer Design Print Ad for Clothing Store

We are a modest women's clothing store. We are looking for a print ad 90*134 mm that is attention grabbing and can serve as a template for us going forward. We cannot use pictures of actual women. We need it to include our logo, store hours, physical address, website, phone number. We would use this template and change the call to action as necessary e. g. BOGO Sale, 30% off, flash sale, summer sale etc. Our colors are black and white and our fonts are Bodoni sans and Athens.

Target Market(s)

Women from teen to age 70

Industry/Entity Type

Women's clothing

Font styles to use
Other font styles liked:
• Athens, Bodoni Sans

Requirements
Must have
• Our, logo, phone number, website, address and store hours
Nice to have
• I'd like something that's not just our flat logo but something that will make someone pause to look
Should not have
• Pictures of women

```html
<!DOCTYPE html>
<html lang="en">
<head>
<meta charset="utf-8">
<title>BOGO Sale Flyer</title>
<link href="https://fonts.googleapis.com/css2?family=Permanent+Marker&family=Tenor+Sans&family=Crimson+Pro:wght@500;600&display=swap" rel="stylesheet">
<style>
  :root {
    --page: #e6e6e6;
    --paper: #ffffff;
    --ink: #141414;
    --band: #454545;
    --on-band: #ffffff;
    --stripe: #111111;
  }
  * { box-sizing: border-box; margin: 0; padding: 0; }
  html, body { width: 900px; height: 1200px; overflow: hidden; background: var(--page); }
  .flyer {
    position: absolute; left: 60px; top: 20px;
    width: 780px; height: 1160px;
    background: var(--paper);
    box-shadow: 0 4px 14px rgba(0,0,0,.18);
    overflow: hidden;
    color: var(--ink);
  }
  .brand { position: absolute; left: 0; width: 100%; top: 30px; text-align: center; }
  .brand-mark { width: 80px; height: 80px; border-radius: 50%; background: var(--ink); margin: 0 auto; }
  .brand-name {
    margin-top: 12px; font-family: "Tenor Sans", sans-serif; font-size: 17px;
    letter-spacing: 6px; color: var(--ink);
  }
  .headline {
    position: absolute; left: 0; width: 100%; text-align: center;
    font-family: "Permanent Marker", "Marker Felt", "Comic Sans MS", cursive;
    font-weight: 400; color: var(--ink); line-height: 1;
  }
  .headline.bogo { top: 148px; font-size: 168px; letter-spacing: -4px; }
  .headline.sale { top: 298px; font-size: 178px; letter-spacing: -4px; }
  .offer-ribbon { position: absolute; left: 93px; top: 491px; width: 614px; height: 97px; }
  .offer-text {
    position: absolute; left: 93px; top: 491px; width: 614px; height: 97px;
    display: flex; align-items: center; justify-content: center;
    font-family: "Tenor Sans", sans-serif; font-size: 78px; color: var(--on-band);
  }
  .stripes { position: absolute; left: 40px; top: 603px; width: 700px; height: 221px; }
  .stripe { position: absolute; left: 0; width: 100%; height: 32px; background: var(--stripe); }
  .gallery { position: absolute; top: 603px; left: 93px; width: 596px; height: 221px; }
  .shot { position: absolute; top: 0; height: 221px; }
  .shot-1 { left: 0; width: 187px; background: linear-gradient(100deg, #d9536f 0%, #b4455c 35%, #3e4752 70%, #cfd3d8 100%); }
  .shot-2 { left: 206px; width: 190px; background: linear-gradient(160deg, #f1ece6 0%, #f08a3a 30%, #3f63b0 60%, #e94f6f 85%, #ede7df 100%); }
  .shot-3 { left: 413px; width: 183px; background: linear-gradient(90deg, #e9c2b4 0%, #d8aa9c 40%, #8d9496 70%, #5b5146 100%); }
  .hours {
    position: absolute; left: 93px; top: 842px; width: 597px; height: 91px;
    background: var(--band); color: var(--on-band);
    font-family: "Tenor Sans", sans-serif; font-size: 31px; line-height: 1.35;
    display: flex; flex-direction: column; align-items: center; justify-content: center;
  }
  .contact { position: absolute; left: 30px; top: 958px; width: 290px; text-align: center; font-family: "Crimson Pro", serif; }
  .icon { display: block; margin: 0 auto; }
  .phone-number { font-size: 40px; font-weight: 500; line-height: 1.1; margin: 4px 0 8px; }
  .website { font-size: 23px; font-weight: 600; margin-top: 4px; }
  .divider { position: absolute; left: 337px; top: 983px; width: 2px; height: 145px; background: var(--ink); }
  .address {
    position: absolute; left: 350px; top: 963px; width: 410px; text-align: center;
    font-family: "Crimson Pro", serif; font-weight: 600; font-size: 25px; line-height: 1.25;
  }
  .address .he { font-weight: 500; font-size: 23px; }
  .address .buses { margin-top: 8px; }
</style>
</head>
<body>
  <main class="flyer">
    <header class="brand">
      <div class="brand-mark"></div>
      <div class="brand-name">MARLOWE</div>
    </header>

    <h1 class="headline bogo">BOGO</h1>
    <h1 class="headline sale">SALE</h1>

    <svg class="offer-ribbon" viewBox="0 0 614 97" aria-hidden="true">
      <polygon points="0,0 614,0 594,48 614,97 0,97 20,48" fill="#454545"/>
    </svg>
    <div class="offer-text">30% OFF</div>

    <div class="stripes" aria-hidden="true">
      <div class="stripe" style="top:10px"></div>
      <div class="stripe" style="top:68px"></div>
      <div class="stripe" style="top:124px"></div>
      <div class="stripe" style="top:180px"></div>
    </div>
    <div class="gallery">
      <div class="shot shot-1" role="img" aria-label="Photo of clothing racks in a boutique with pink blouses"></div>
      <div class="shot shot-2" role="img" aria-label="Photo of colourful tops on hangers"></div>
      <div class="shot shot-3" role="img" aria-label="Photo of blush and grey coats on a rail"></div>
    </div>

    <section class="hours">
      <div>S-TH- 10:30-12:30 - <span dir="rtl">א-ה</span></div>
      <div>20:30 - 22:30</div>
    </section>

    <section class="contact">
      <svg class="icon" width="34" height="34" viewBox="0 0 24 24" aria-hidden="true">
        <path fill="#141414" d="M6.6 10.8a15.1 15.1 0 0 0 6.6 6.6l2.2-2.2c.3-.3.7-.4 1-.2 1.1.4 2.3.6 3.6.6.6 0 1 .4 1 1V20c0 .6-.4 1-1 1C10.6 21 3 13.4 3 4c0-.6.4-1 1-1h3.5c.6 0 1 .4 1 1 0 1.3.2 2.5.6 3.6.1.3 0 .7-.2 1z"/>
      </svg>
      <div class="phone-number">1.720.555.0188</div>
      <svg class="icon" width="28" height="28" viewBox="0 0 24 24" aria-hidden="true">
        <circle cx="12" cy="12" r="10" fill="#141414"/>
        <g fill="none" stroke="#fff" stroke-width="1.3">
          <ellipse cx="12" cy="12" rx="4.5" ry="10"/>
          <line x1="2" y1="12" x2="22" y2="12"/>
          <path d="M4 7h16M4 17h16"/>
        </g>
      </svg>
      <div class="website">www.marlowestyle.com</div>
    </section>

    <div class="divider"></div>

    <section class="address">
      <div>Cedar Hill Shopping Center</div>
      <div class="he" dir="rtl">(מעל בית הקפה)</div>
      <div class="he" dir="rtl">ניתן להגיע גם משדרות הארזים 16</div>
      <div class="buses">Buses 12, 18, 27, 33, 48, 54, 61,<br>70, 73, 84, 90</div>
    </section>
  </main>
</body>
</html>
```